Income Tax and Accounting Brochure

I need a brochure using my new logo (file attached). I do tax work and accounting work. I am an EA (QDX Enrolled Agent - logo attached) and would like this incorporated into the brochure. I also have a MSA in Accounting. Please incorporate the text that I have provided in the brochure.

Target Market(s)

Tax Clients - both business and individuals

Industry/Entity Type

Accounting

Colors
0054AA
0677BA
7BADD7
CADEEF
E8F1F8

Requirements
Must have
• Use my logo and the QDX EA file in the brochure
Nice to have
• I would like to see a brochure that I can customize with my own text if possible.

```html
<!DOCTYPE html>
<html lang="en">
<head>
<meta charset="utf-8">
<title>Vale Accounting &amp; Consulting – Income Tax &amp; Accounting</title>
<link href="https://fonts.googleapis.com/css2?family=Heebo:wght@300;700;800&family=Open+Sans:ital,wght@0,400;1,700&display=swap" rel="stylesheet">
<style>
  :root {
    --backdrop: #efefef;
    --paper: #ffffff;
    --brand-blue: #1656a4;
    --banner-blue: #0f78bb;
    --accent-red: #c0152f;
    --ink: #1e1e1e;
    --rule: #8a8a8a;
    --photo-light: #f7efdf;
    --photo-mid: #e6d8c2;
    --photo-cool: #c6d4e2;
  }
  * { margin: 0; padding: 0; box-sizing: border-box; }
  html, body { width: 1200px; height: 1200px; overflow: hidden; }
  body { background: var(--backdrop); font-family: "Open Sans", sans-serif; color: var(--ink); position: relative; }

  .brochure {
    position: absolute; left: 229px; top: 57px;
    width: 756px; height: 1060px;
    background: var(--paper); overflow: hidden;
  }

  .hero-art { position: absolute; left: 0; top: 0; width: 756px; height: 560px; }

  .brand { position: absolute; left: 39px; top: 66px; display: flex; align-items: center; gap: 10px; }
  .brand-mark { width: 70px; height: 70px; border-radius: 50%; background: var(--brand-blue); flex: none; }
  .brand-name {
    font-family: "Heebo", sans-serif; font-weight: 700; color: var(--brand-blue);
    font-size: 19px; line-height: 27px; letter-spacing: 0.8px; white-space: nowrap;
  }
  .brand-line2 { display: block; font-size: 15px; letter-spacing: 2.6px; }

  .banner-title {
    position: absolute; left: 36px; top: 214px; color: #fff;
    font-family: "Heebo", sans-serif; font-weight: 800;
    font-size: 38px; line-height: 38px; letter-spacing: -0.3px;
  }
  .banner-sub {
    position: absolute; left: 36px; top: 296px; color: #fff;
    font-family: "Heebo", sans-serif; font-weight: 300;
    font-size: 21px; line-height: 20px;
  }

  .column-rule { position: absolute; left: 308px; top: 404px; width: 1px; height: 516px; background: var(--rule); }

  .about { position: absolute; left: 38px; top: 424px; width: 256px; }
  .about-kicker { font-family: "Heebo", sans-serif; font-weight: 300; font-size: 27px; line-height: 28px; color: #333; }
  .about-name {
    font-family: "Heebo", sans-serif; font-weight: 800; color: var(--brand-blue);
    font-size: 25.5px; line-height: 26px; margin-bottom: 14px; letter-spacing: -0.3px;
  }

  .copy { font-size: 12.3px; line-height: 14.8px; letter-spacing: -0.15px; }
  .about .copy { font-size: 12.6px; letter-spacing: -0.1px; }
  .copy p { margin-bottom: 10px; }

  .section-label {
    font-family: "Open Sans", sans-serif; font-style: italic; font-weight: 700;
    color: var(--accent-red); font-size: 14.5px; line-height: 18px; margin: 4px 0 6px;
  }

  .services { position: absolute; left: 325px; top: 500px; width: 400px; }
  .services-title {
    font-family: "Heebo", sans-serif; font-weight: 800; color: var(--brand-blue);
    font-size: 19px; line-height: 20px; margin-bottom: 10px;
  }
  .services .copy p { margin-bottom: 5px; }
  .services .section-label { margin-top: 10px; }

  .benefits { list-style: none; }
  .benefits li { position: relative; padding-left: 12px; margin-bottom: 8px; }
  .benefits li::before {
    content: ""; position: absolute; left: 1px; top: 5px;
    width: 6px; height: 6px; border-radius: 50%; background: var(--ink);
  }

  .footer-rule { position: absolute; left: 0; top: 962px; width: 756px; height: 4px; background: var(--accent-red); }
  .footer { position: absolute; left: 0; top: 966px; width: 756px; height: 94px; background: var(--brand-blue); color: #fff; }
  .appointment { position: absolute; left: 51px; top: 12px; width: 220px; text-align: center; }
  .appointment-label { font-family: "Heebo", sans-serif; font-weight: 300; font-size: 16px; line-height: 20px; }
  .appointment-phone { font-family: "Heebo", sans-serif; font-weight: 800; font-size: 21px; line-height: 26px; }

  .contact { position: absolute; font-family: "Heebo", sans-serif; font-weight: 300; font-size: 15px; line-height: 18px; display: flex; align-items: center; gap: 6px; white-space: nowrap; }
  .contact svg { width: 15px; height: 15px; flex: none; }
  .contact-address { left: 335px; top: 10px; }
  .contact-web { left: 335px; top: 36px; }
  .contact-mail { left: 514px; top: 36px; }
</style>
</head>
<body>
  <main class="brochure">
    <svg class="hero-art" viewBox="0 0 756 560">
      <defs>
        <radialGradient id="photo-tone" cx="0.45" cy="0.3" r="0.8">
          <stop offset="0" stop-color="var(--photo-light)"/>
          <stop offset="0.55" stop-color="var(--photo-mid)"/>
          <stop offset="1" stop-color="var(--photo-cool)"/>
        </radialGradient>
      </defs>
      <rect class="banner" x="0" y="189" width="340" height="175" fill="var(--banner-blue)"/>
      <circle cx="540" cy="241" r="248" fill="var(--paper)"/>
      <circle class="hero-ring" cx="540" cy="241" r="232" fill="var(--brand-blue)"/>
      <circle class="hero-photo" cx="556" cy="222" r="206" fill="url(#photo-tone)" role="img"
              aria-label="Photo of two professionals at a desk reviewing financial charts with pens and a calculator"/>
    </svg>

    <div class="brand">
      <span class="brand-mark"></span>
      <div class="brand-name">VALE ACCOUNTING<span class="brand-line2">&amp; CONSULTING, LLC</span></div>
    </div>

    <h1 class="banner-title">INCOME TAX &amp;<br>ACCOUNTING</h1>
    <p class="banner-sub">for Individual and<br>Businesses</p>

    <div class="column-rule"></div>

    <section class="about">
      <p class="about-kicker">About</p>
      <h2 class="about-name">Marion T Caldwell,<br>MSA EA (Principal)</h2>
      <div class="copy">
        <p>I have a Masters' Degree in accounting and am an QDX Enrolled Agent. I am also a LedgerPro Advanced Certified Consultant in both the online and desktop products including Enterprise and Point of Sale. I provide individual and small business tax services, Accounting, bookkeeping, QDX representation, insurance audit representation, business license assistance and more.</p>
        <p>I have experience working with a wide variety of clients from the point where they first decide they want to start a business. They are often unsure about what to do first- I have a lot of experience to offer you.</p>
        <h3 class="section-label">Books a Mess: No Problem!</h3>
        <p>If you own a small business and haven't kept up your bookkeeping, don't worry. We can help you. We'll prepare your bookkeeping for the year, prepare a full Schedule C, as well as your personal income tax return. Then we'll help you set up an easy system that allows you to keep your books in tip-top shape next year.</p>
      </div>
    </section>

    <section class="services">
      <h2 class="services-title">What a joy it is to<br>watch success in action!</h2>
      <div class="copy">
        <h3 class="section-label">Tax Preparation – why hire us?</h3>
        <p>Preparing your own income tax return can be a task that leaves you with more questions than answers. According to a study released by the National Revenue Review Office last year, most taxpayers (77% of 71 million taxpayers) believe they benefited from using a professional tax preparer.</p>
        <p>Whether we like it or not, today's tax laws are so complicated that filing a relatively simple return can be confusing. It is just too easy to overlook deductions and credits to which you are entitled. Even if you use a computer software program there's no substitute for the assistance of an experienced tax professional.</p>
        <h3 class="section-label">Here's what your get...</h3>
        <ul class="benefits">
          <li>Your tax return will be checked and rechecked by our computer software identifying potential problems the QDX may look at more closely and reviewing the math to limit QDX contacts.</li>
          <li>Your tax return can be filed electronically so you will get a refund back quicker.</li>
          <li>Our staff will show you how to adjust your payroll withholding to get more money back each week. Why give the QDX an interest free loan for up to 16 months.</li>
          <li>We will show you potential deductions to limit your tax liability for next year. In addition, we will give you a sheet of commonly overlooked deductions to limit the following year's tax liability.</li>
        </ul>
      </div>
    </section>

    <div class="footer-rule"></div>
    <footer class="footer">
      <div class="appointment">
        <p class="appointment-label">Call for appointment</p>
        <p class="appointment-phone">(555-010-4821)</p>
      </div>
      <p class="contact contact-address">
        <svg viewBox="0 0 16 16" fill="none" stroke="#fff" stroke-width="1.2"><path d="M8 15s5-5 5-9a5 5 0 0 0-10 0c0 4 5 9 5 9z"/><circle cx="8" cy="6" r="2"/></svg>
        2158, Harbor Lane Avenue, Fairview 412
      </p>
      <p class="contact contact-web">
        <svg viewBox="0 0 16 16" fill="none" stroke="#fff" stroke-width="1.1"><circle cx="8" cy="8" r="6.5"/><ellipse cx="8" cy="8" rx="3" ry="6.5"/><path d="M1.5 8h13M2.5 4.5h11M2.5 11.5h11"/></svg>
        www.valeacct.example
      </p>
      <p class="contact contact-mail">
        <svg viewBox="0 0 16 16" fill="none" stroke="#fff" stroke-width="1.1"><rect x="1.5" y="4" width="13" height="9.5"/><path d="M1.5 4l6.5 5 6.5-5"/></svg>
        info@valeacct.example
      </p>
    </footer>
  </main>
</body>
</html>
```